Need Business cards

Im a new realtor and already have a logo. I would like to purchase a Business card design that catches customer's attention, its creative, and modern.

Marisol Vandera
Realtor ®
(555) 214 7730
marisolvndrealtor@brightmailbox.com

Target Market(s)

investors, buyers and seller, property management

Industry/Entity Type

real estate,

Contact Information for Business Card

Marisol Vandera

Requirements
Must have
• BOTH LOGOS, WOULD LIKE TO SEE WITH DIFFERENT OPTIONS WITH EITHER PICTURE

```html
<!DOCTYPE html>
<html lang="en">
<head>
<meta charset="utf-8">
<title>Marisol Vandera – Realtor Business Card</title>
<link rel="stylesheet" href="https://fonts.googleapis.com/css2?family=Montserrat:wght@400;500;600&display=swap">
<style>
  :root {
    --page-bg: #e4e4e4;
    --card-dark: #1c1c1c;
    --gold: #cfa52c;
    --gold-light: #f6dd7a;
    --gold-deep: #b07f14;
    --text-light: #f2f2f2;
  }
  * { margin: 0; padding: 0; box-sizing: border-box; }
  html, body {
    width: 1200px; height: 1181px; overflow: hidden;
    background: var(--page-bg);
    font-family: "Montserrat", sans-serif;
  }
  .card {
    position: absolute;
    left: 241px;
    width: 719px; height: 411px;
    background: var(--card-dark);
    border-radius: 22px;
    overflow: hidden;
  }
  .card--front { top: 164px; }
  .card--back { top: 620px; }

  .front-art { position: absolute; inset: 0; }

  .brand {
    position: absolute;
    display: flex; flex-direction: column; align-items: center;
    color: var(--gold);
  }
  .brand__mark {
    border: 4px solid var(--gold);
  }
  .brand__name {
    font-weight: 500; letter-spacing: 0.4px; white-space: nowrap;
  }
  .brand__role {
    display: flex; align-items: center; gap: 6px;
    font-weight: 400; letter-spacing: 0.4px;
  }
  .brand__role::before, .brand__role::after {
    content: ""; height: 1px; background: var(--gold);
  }

  .card--front .brand { left: 20px; width: 320px; top: 108px; }
  .card--front .brand__mark { width: 80px; height: 80px; margin-bottom: 18px; }
  .card--front .brand__name { font-size: 17px; }
  .card--front .brand__role { font-size: 12.5px; margin-top: 4px; }
  .card--front .brand__role::before,
  .card--front .brand__role::after { width: 50px; }

  .card--back .brand { left: 0; width: 719px; top: 140px; }
  .card--back .brand__mark { width: 100px; height: 100px; border-width: 5px; margin-bottom: 24px; }
  .card--back .brand__name { font-size: 22px; }
  .card--back .brand__role { font-size: 16px; margin-top: 4px; }
  .card--back .brand__role::before,
  .card--back .brand__role::after { width: 64px; }

  .contact {
    position: absolute; left: 44px; top: 301px;
    list-style: none; color: var(--text-light);
  }
  .contact__item {
    display: flex; align-items: center; gap: 10px;
    height: 34px;
  }
  .contact__icon { width: 22px; height: 22px; flex: none; }
  .contact__phone { font-size: 18px; }
  .contact__email { font-size: 15.5px; letter-spacing: -0.1px; }
</style>
</head>
<body>

<section class="card card--front">
  <svg class="front-art" width="719" height="411" viewBox="0 0 719 411">
    <defs>
      <linearGradient id="goldBand" x1="0" y1="0" x2="0" y2="1">
        <stop offset="0" stop-color="#c99a20"/>
        <stop offset="0.4" stop-color="#f6dd7a"/>
        <stop offset="0.7" stop-color="#d9ad3a"/>
        <stop offset="1" stop-color="#b07f14"/>
      </linearGradient>
      <linearGradient id="photoBase" x1="0" y1="0" x2="0" y2="1">
        <stop offset="0" stop-color="#f7f8fb"/>
        <stop offset="1" stop-color="#eef0f4"/>
      </linearGradient>
      <radialGradient id="photoHair" cx="0.52" cy="0.42" r="0.42">
        <stop offset="0" stop-color="#d9b48c" stop-opacity="0.95"/>
        <stop offset="0.45" stop-color="#c9a074" stop-opacity="0.7"/>
        <stop offset="1" stop-color="#c9a074" stop-opacity="0"/>
      </radialGradient>
      <radialGradient id="photoBlazer" cx="0.78" cy="0.95" r="0.55">
        <stop offset="0" stop-color="#f1d7a6"/>
        <stop offset="0.55" stop-color="#f3ddb4" stop-opacity="0.8"/>
        <stop offset="1" stop-color="#f3ddb4" stop-opacity="0"/>
      </radialGradient>
      <clipPath id="photoClip">
        <polygon points="437,0 719,0 719,411 440,411 375,201"/>
      </clipPath>
    </defs>
    <g role="img" aria-label="Portrait photo of the realtor in a cream blazer against a white backdrop" clip-path="url(#photoClip)">
      <rect x="370" y="0" width="349" height="411" fill="url(#photoBase)"/>
      <rect x="370" y="0" width="349" height="411" fill="url(#photoBlazer)"/>
      <rect x="370" y="0" width="349" height="411" fill="url(#photoHair)"/>
    </g>
    <polygon points="403,0 437,0 375,201 440,411 403,411 341,201" fill="url(#goldBand)"/>
    <rect class="badge" x="662" y="344" width="28" height="28" fill="#ffffff" opacity="0.92"/>
  </svg>

  <div class="brand">
    <div class="brand__mark"></div>
    <div class="brand__name">MARISOL VANDERA</div>
    <div class="brand__role">REALTOR</div>
  </div>

  <ul class="contact">
    <li class="contact__item">
      <svg class="contact__icon" viewBox="0 0 22 22" aria-hidden="true">
        <circle cx="11" cy="11" r="10" fill="none" stroke="var(--gold)" stroke-width="1.6"/>
        <path d="M8 6.5c.6-.4 1.1-.3 1.4.3l.7 1.4c.2.5 0 .9-.4 1.2l-.5.4c.5 1.1 1.4 2 2.5 2.5l.4-.5c.3-.4.7-.6 1.2-.4l1.4.7c.6.3.7.8.3 1.4-.7 1-1.8 1.3-3 .7-2-1-3.5-2.5-4.5-4.5-.6-1.2-.3-2.3.5-3.2z" fill="var(--gold)"/>
      </svg>
      <span class="contact__phone">(555) 214 7730</span>
    </li>
    <li class="contact__item">
      <svg class="contact__icon" viewBox="0 0 22 22" aria-hidden="true">
        <circle cx="11" cy="11" r="10" fill="none" stroke="var(--gold)" stroke-width="1.6"/>
        <rect x="6.5" y="8" width="9" height="6.5" rx="0.8" fill="var(--gold)"/>
        <path d="M6.8 8.4l4.2 3.2 4.2-3.2" fill="none" stroke="var(--card-dark)" stroke-width="0.9"/>
      </svg>
      <span class="contact__email">marisolvndrealtor@brightmailbox.com</span>
    </li>
  </ul>
</section>

<section class="card card--back">
  <div class="brand">
    <div class="brand__mark"></div>
    <div class="brand__name">MARISOL VANDERA</div>
    <div class="brand__role">REALTOR</div>
  </div>
</section>

</body>
</html>
```